New London based construction company website

We need a website designing for our new London based construction company which aims to provide total & fernway yard services.

The website is to have two sides to it one for "halcrest build services" and one for "fernway yard services" with an opening page with both logo's to choose from.

Would like the website to be modern, professional and inspire confidence.

Target Market(s)

Those specifically visiting the site to check that the company is professional

Industry/Entity Type

Construction

Contact Information for Business Card

One side for Fernway Yard Services the other Halcrest Build Services

Number of Pages Required

5+ page

Font styles to use
Sans Serif

Requirements
Must have
• The website is to have two sides to it one for "halcrest build services" and one for "fernway yard services" with an opening page with both logo's to choose from.

```html
<!DOCTYPE html>
<html lang="en">
<head>
<meta charset="utf-8">
<title>Halcrest Build Services</title>
<link rel="stylesheet" href="https://fonts.googleapis.com/css2?family=Open+Sans:wght@400;600;700;800&display=swap">
<style>
  :root {
    --blue: #1b5fa0;
    --title-blue: #1c5a94;
    --sky-top: #1d3f7a;
    --sky-mid: #3f6fb0;
    --steel: #6f7f92;
    --ink: #333;
    --muted: #666;
    --soft-bg: #f6f6f6;
    --tab: #8c8c8c;
    --white: #fff;
  }
  * { box-sizing: border-box; margin: 0; padding: 0; }
  html, body { width: 739px; height: 1200px; overflow: hidden; }
  body { font-family: "Open Sans", Arial, sans-serif; color: var(--ink); background: var(--white); position: relative; }

  .hero {
    position: absolute; left: 0; top: 0; width: 739px; height: 349px;
    background: linear-gradient(160deg, var(--sky-top) 0%, var(--sky-mid) 40%, var(--steel) 75%, #8a6a3f 100%);
  }
  .hero-arrow { position: absolute; top: 166px; }
  .hero-arrow.prev { left: 14px; }
  .hero-arrow.next { right: 14px; }
  .brand-box {
    position: absolute; left: 271px; top: 67px; width: 197px; height: 99px;
    background: rgba(255,255,255,0.94); border-radius: 2px;
    display: flex; align-items: center; justify-content: center; gap: 8px;
  }
  .brand-mark { width: 12px; height: 12px; background: var(--blue); flex: none; }
  .brand-name { font-size: 12px; font-weight: 600; color: #5a6470; letter-spacing: 0.5px; }
  .hero-title {
    position: absolute; left: 0; width: 739px; top: 201px; text-align: center;
    color: var(--white); font-weight: 800; font-size: 20px; line-height: 25px;
  }
  .hero-btn {
    position: absolute; left: 337px; top: 257px; width: 65px; height: 25px;
    border: 1px solid var(--white); color: var(--white); font-size: 7.5px;
    display: flex; align-items: center; justify-content: center;
  }

  .main-nav { position: absolute; left: 0; top: 349px; width: 739px; height: 29px; background: var(--blue); }
  .main-nav a { position: absolute; top: 0; height: 29px; line-height: 29px; color: var(--white); font-size: 8px; font-weight: 600; text-decoration: none; transform: translateX(-50%); white-space: nowrap; }
  .main-nav a.active { left: 81px; width: 77px; transform: none; text-align: center; background: var(--tab); }

  .welcome { position: absolute; left: 81px; top: 422px; width: 577px; text-align: center; }
  .section-title { color: var(--title-blue); font-weight: 700; font-size: 14.5px; }
  .welcome p { margin-top: 5px; font-size: 6.5px; line-height: 13.6px; color: var(--muted); }

  .featured { position: absolute; left: 0; top: 547px; width: 739px; height: 271px; background: var(--soft-bg); }
  .block-head { position: absolute; left: 81px; width: 577px; display: flex; justify-content: space-between; align-items: center; }
  .pager { display: flex; gap: 2px; }
  .pager span { width: 16px; height: 15px; display: flex; align-items: center; justify-content: center; }
  .pager .back { background: #8a8a8a; }
  .pager .fwd { background: #222; }
  .project { position: absolute; top: 68px; width: 134px; }
  .project .photo { width: 134px; height: 135px; }
  .project p { margin-top: 8px; font-size: 8.6px; line-height: 12.5px; color: var(--muted); }

  .blog-post { position: absolute; top: 897px; width: 184px; }
  .blog-post .photo { width: 184px; height: 98px; }
  .blog-post h3 { margin-top: 12px; font-size: 8.6px; font-weight: 400; line-height: 12px; color: var(--ink); }
  .blog-post time { display: block; margin-top: 5px; font-size: 6px; color: var(--ink); }
  .blog-post p { margin-top: 6px; font-size: 6px; line-height: 10.8px; color: var(--muted); text-align: justify; }
  .blog-post .more { display: block; margin-top: 2px; font-size: 6px; color: var(--ink); }

  .site-footer { position: absolute; left: 0; top: 1140px; width: 739px; height: 60px; background: var(--blue); color: var(--white); }
  .footer-links { position: absolute; left: 81px; top: 17px; font-size: 6px; }
  .footer-links span { margin: 0 4px; }
  .copyright { position: absolute; left: 81px; top: 34px; font-size: 6px; }
  .social { position: absolute; left: 582px; top: 18px; display: flex; gap: 7px; }
  .social span { width: 20px; height: 20px; border-radius: 50%; background: var(--white); }
</style>
</head>
<body>
  <header class="hero" role="img" aria-label="Photo looking up at glass buildings under construction with a tower crane against a blue sky">
    <svg class="hero-arrow prev" width="10" height="16" viewBox="0 0 10 16"><path d="M8 1 L2 8 L8 15" fill="none" stroke="#fff" stroke-width="1.6"/></svg>
    <svg class="hero-arrow next" width="10" height="16" viewBox="0 0 10 16"><path d="M2 1 L8 8 L2 15" fill="none" stroke="#fff" stroke-width="1.6"/></svg>
    <div class="brand-box"><span class="brand-mark"></span><span class="brand-name">Halcrest Build Services</span></div>
    <h1 class="hero-title">NULLAM ORNARE TORTOR<br>METUS VARIUS</h1>
    <a class="hero-btn">READ MORE</a>
  </header>

  <nav class="main-nav">
    <a class="active">HOME</a>
    <a style="left:210px">ABOUT US</a>
    <a style="left:306px">SERVICES</a>
    <a style="left:405px">SOLUTIONS</a>
    <a style="left:505px">PROJECTS</a>
    <a style="left:606px">CONTACT US</a>
  </nav>

  <section class="welcome">
    <h2 class="section-title">WELCOME TO HALCREST BUILD SERVICES</h2>
    <p>Donec vestibulum tempus orci. Aenean id erat tempor, venenatis orci eget, iaculis est. Lorem ipsum dolor sit amet, consectetur adipiscing elit. Donec lobortis eros quis ante tincidunt rutrum. Nullam ornare tortor a metus varius imperdiet. Cras in enim vel mi eleifend fringilla vel et ante. Vivamus tellus metus, convallis et neque tempus, posuere pellentesque sapien. Vivamus pellentesque interdum risus id rhoncus. Quisque finibus nisi vel lacinia porta. Donec feugiat sed elit eget facilisis. Vivamus vel turpis a tellus ornare rhoncus ut quis quam. Donec eleifend vulputate euismod. Sed varius magna nec enim posuere molestie. Aliquam pharetra id nisi quis facilisis.</p>
  </section>

  <section class="featured">
    <div class="block-head" style="top:38px">
      <h2 class="section-title">FEATURED PROJECTS</h2>
      <div class="pager">
        <span class="back"><svg width="8" height="8" viewBox="0 0 8 8"><path d="M7 4H1M4 1L1 4L4 7" fill="none" stroke="#fff" stroke-width="1.2"/></svg></span>
        <span class="fwd"><svg width="8" height="8" viewBox="0 0 8 8"><path d="M1 4H7M4 1L7 4L4 7" fill="none" stroke="#fff" stroke-width="1.2"/></svg></span>
      </div>
    </div>
    <article class="project" style="left:81px">
      <div class="photo" role="img" aria-label="Excavator working on a muddy construction site" style="background:linear-gradient(160deg,#8d8473,#6b6152 60%,#a09784)"></div>
      <p>Pellentesque consequat conse quat dictum.</p>
    </article>
    <article class="project" style="left:228px">
      <div class="photo" role="img" aria-label="Tower crane beside a concrete high-rise under blue sky" style="background:linear-gradient(180deg,#2f5fb0,#4d78c0 50%,#6d6a66)"></div>
      <p>Pellentesque consequat conse quat dictum.</p>
    </article>
    <article class="project" style="left:375px">
      <div class="photo" role="img" aria-label="Scaffolding and steel reinforcement bars on a site" style="background:linear-gradient(180deg,#7d8a6a,#9a8050 60%,#b28d45)"></div>
      <p>Pellentesque consequat conse quat dictum.</p>
    </article>
    <article class="project" style="left:522px">
      <div class="photo" role="img" aria-label="Lit glass office tower at night" style="background:linear-gradient(160deg,#1b2a44,#3d4a52 50%,#b89a4a)"></div>
      <p>Pellentesque consequat conse quat dictum.</p>
    </article>
  </section>

  <div class="block-head" style="top:866px">
    <h2 class="section-title">BLOG</h2>
    <div class="pager">
      <span class="back"><svg width="8" height="8" viewBox="0 0 8 8"><path d="M7 4H1M4 1L1 4L4 7" fill="none" stroke="#fff" stroke-width="1.2"/></svg></span>
      <span class="fwd"><svg width="8" height="8" viewBox="0 0 8 8"><path d="M1 4H7M4 1L7 4L4 7" fill="none" stroke="#fff" stroke-width="1.2"/></svg></span>
    </div>
  </div>

  <article class="blog-post" style="left:81px">
    <div class="photo" role="img" aria-label="Two site engineers in hard hats and high-visibility vests reviewing plans" style="background:linear-gradient(160deg,#b8a894,#e2dccf 50%,#a7b04c)"></div>
    <h3>Pellentesque pulvinar posuere velit et. Cura bitur sollicitudin efficitur egestas</h3>
    <time>30 Mar, 2017</time>
    <p>Donec eget rhoncus nulla. Suspendisse tincidunt commodo cursus. Duis finibus tortor sapien, vel commodo augue tempor eu...</p>
    <a class="more">More</a>
  </article>
  <article class="blog-post" style="left:278px">
    <div class="photo" role="img" aria-label="Video still of an apartment tower lit up at night" style="background:linear-gradient(180deg,#141a2c,#3b3440 60%,#6b5430)">
      <svg width="184" height="98" viewBox="0 0 184 98"><circle cx="92" cy="49" r="12" fill="#fff"/><path d="M88 42 L98 49 L88 56 Z" fill="#222"/></svg>
    </div>
    <h3>Pellentesque pulvinar posuere velit et. Cura bitur sollicitudin efficitur egestas</h3>
    <time>30 Mar, 2017</time>
    <p>Donec eget rhoncus nulla. Suspendisse tincidunt commodo cursus. Duis finibus tortor sapien, vel commodo augue tempor eu...</p>
    <a class="more">More</a>
  </article>
  <article class="blog-post" style="left:474px">
    <div class="photo" role="img" aria-label="Two workers checking drawings inside a bright office fit-out" style="background:linear-gradient(160deg,#e8ecef,#cfd6dc 60%,#b9b39a)"></div>
    <h3>Pellentesque pulvinar posuere velit et. Cura bitur sollicitudin efficitur egestas</h3>
    <time>30 Mar, 2017</time>
    <p>Donec eget rhoncus nulla. Suspendisse tincidunt commodo cursus. Duis finibus tortor sapien, vel commodo augue tempor eu...</p>
    <a class="more">More</a>
  </article>

  <footer class="site-footer">
    <div class="footer-links">Home<span>|</span>About Us<span>|</span>Services<span>|</span>Solutions<span>|</span>Projects<span>|</span>Contact us</div>
    <div class="copyright">Copyright &copy; 2017 &nbsp;Company name. &nbsp;All rights reserved.</div>
    <div class="social" aria-label="Social links">
      <span></span><span></span><span></span>
    </div>
  </footer>
</body>
</html>
```